TKN Music Studios

I need a website for two locations, description of services, possible merchandise page, PDFs of faculty, bios, live performance of both faculty and students, testimonial page, pre-college prep page for musical theatre, links to our social media, link to our registration page, link to affiliate programming resources

```html
<!DOCTYPE html>
<html lang="en">
<head>
<meta charset="utf-8">
<title>TKN Music Studios</title>
<link rel="stylesheet" href="https://fonts.googleapis.com/css2?family=Playfair+Display:wght@700;900&family=Roboto:ital,wght@0,400;0,500;0,700;1,400&display=swap">
<style>
:root{
  --purple:#7c2cf2;
  --magenta:#b12fe0;
  --slate:#8189b3;
  --ink:#14142b;
  --navy:#0b0a26;
  --grey-text:#7d8096;
  --card:#f2f3f7;
  --white:#ffffff;
  --serif:'Playfair Display', Georgia, serif;
  --sans:'Roboto', Arial, sans-serif;
}
*{box-sizing:border-box;margin:0;padding:0}
html,body{width:1200px;height:4710px;overflow:hidden;background:var(--white)}
body{font-family:var(--sans);color:var(--ink)}
.page{position:relative;width:1200px;height:4710px;overflow:hidden}
.abs{position:absolute}
.backdrop{position:absolute;left:0;top:0;width:1200px;height:4710px}
h1,h2,h3,h4{font-family:var(--serif);font-weight:900}
.brand{left:240px;top:22px;display:flex;align-items:center;gap:8px;color:var(--white);font-family:var(--sans);font-weight:700;font-size:11px;line-height:1.15}
.brand-dot{width:26px;height:26px;border-radius:50%;border:2px solid var(--white)}
.nav{left:452px;top:30px;display:flex;gap:0;font-size:7.5px;font-weight:700;color:var(--white);letter-spacing:.2px}
.nav a{color:inherit;text-decoration:none;margin-right:26px}
.hero-title{left:240px;top:268px;color:var(--white);font-size:32px;line-height:1.02}
.hero-sub{left:240px;top:345px;color:var(--white);font-size:8.5px}
.hero-art{left:740px;top:140px;width:160px;height:380px;border-radius:80px;background:linear-gradient(160deg,#e1d7f2,#b8a6d8 60%,#d9cfee)}
.hero-dot{left:672px;top:264px;width:20px;height:28px;border-radius:14px 0 0 14px;background:#c8b6f6}
.perk{width:180px;font-size:8.5px;color:var(--grey-text);line-height:1.65}
.perk h4{font-size:10px;color:var(--ink);margin-bottom:8px;display:flex;align-items:center;gap:10px;font-family:var(--serif)}
.perk p{padding-left:34px}
.section-title{font-size:27px;line-height:1.18;color:var(--ink)}
.lead{font-size:8.5px;color:var(--grey-text);line-height:1.65}
.pager{display:flex;gap:14px;font-size:7px;color:#b7b9c7;letter-spacing:.5px}
.pager span{display:flex;flex-direction:column;gap:2px}
.pager i{display:block;width:32px;height:1px;background:currentColor}
.course{width:203px;height:285px;background:#f5f1ee;border:1px solid #d8d2cf;text-align:center;font-size:10px;color:#5a5560;line-height:1.2}
.course .shot{height:146px;background:linear-gradient(135deg,#2a0d1e,#8e1d3a 45%,#3b1340)}
.course p{margin:22px 18px 0}
.course p + p{margin-top:18px}
.white-title{color:var(--white);font-size:27px;line-height:1.18}
.white-lead{color:var(--white);font-size:8.5px;line-height:1.7}
.video{left:608px;top:1222px;width:352px;height:240px;background:linear-gradient(120deg,#5d6a7a,#a6a096 50%,#7a5a4c)}
.play{left:760px;top:1317px;width:44px;height:44px;border-radius:50%;background:var(--purple);display:flex;align-items:center;justify-content:center}
.service{width:228px;height:212px;background:var(--card);padding:46px 26px 0;font-size:8.5px;color:var(--grey-text);line-height:1.7}
.service h4{font-size:10.5px;color:var(--ink);margin:14px 0 10px}
.service.raised{background:var(--white);box-shadow:0 18px 40px rgba(20,20,60,.12)}
.quote-mark{left:240px;top:2748px;font-size:22px;color:var(--purple);font-weight:500}
.quote{left:240px;top:2798px;width:290px;font-style:italic;font-size:11.5px;color:#8a8da6;line-height:1.8}
.person{left:240px;top:2905px;font-family:var(--serif);font-weight:700;font-size:10px}
.role{left:240px;top:2925px;font-size:7px;color:var(--grey-text)}
.portrait{left:610px;top:2665px;width:350px;height:390px;background:linear-gradient(160deg,#6b5040,#a88b74 50%,#d9d3cb)}
.signup{left:733px;top:3255px;width:228px;height:275px;background:var(--white);box-shadow:0 20px 50px rgba(120,40,220,.25);text-align:center;padding-top:28px}
.signup h3{font-size:14px;color:var(--white);position:relative;top:-30px}
.signup small{display:block;font-size:8px;color:var(--white);position:relative;top:-30px}
.field{margin:0 auto;width:150px;border-bottom:1px solid #e0e0ea;font-size:7px;color:#b3b5c6;text-align:left;padding:16px 0 5px}
.btn{margin:26px auto 0;width:163px;height:30px;background:linear-gradient(90deg,var(--purple),var(--magenta));color:var(--white);font-size:7px;font-weight:700;display:flex;align-items:center;justify-content:center}
.stage{background:linear-gradient(160deg,#2b2230,#6e4c5e 45%,#1d1826)}
.tag{width:96px;height:80px;background:#e6e6e6;border:1px solid #c9c9c9;font-size:11px;color:#555;display:flex;align-items:center;justify-content:center}
.foot-col h4{font-size:12px;color:var(--white);margin-bottom:26px}
.foot-col a{display:block;font-size:8px;color:#a4a6c2;text-decoration:none;margin-bottom:16px}
.news-input{left:733px;top:4474px;width:126px;height:24px;background:#1b1a3c;font-size:7.5px;color:#8b8db0;padding:8px 6px}
.news-btn{left:859px;top:4474px;width:56px;height:24px;background:var(--purple);font-size:6.5px;color:var(--white);font-weight:700;display:flex;align-items:center;justify-content:center}
.social{top:4618px;width:24px;height:24px;background:#2a2948}
.copy{left:240px;top:4626px;font-size:8px;color:var(--white)}
</style>
</head>
<body>
<div class="page">

<svg class="backdrop" viewBox="0 0 1200 4710" aria-hidden="true">
  <defs>
    <linearGradient id="violet" x1="0" y1="0" x2="1" y2="0">
      <stop offset="0" stop-color="#7b2ff5"/>
      <stop offset="1" stop-color="#b22ee0"/>
    </linearGradient>
  </defs>
  <path d="M0,395 C120,380 200,440 300,470 C420,505 470,445 570,440 C660,436 700,480 800,520 C900,560 1080,640 1200,650 V0 H0 Z" fill="#9aa1c6" transform="translate(0,14)"/>
  <path d="M0,395 C120,380 200,440 300,470 C420,505 470,445 570,440 C660,436 700,480 800,520 C900,560 1080,640 1200,650 V0 H0 Z" fill="url(#violet)"/>
  <path d="M0,1255 C100,1200 220,1300 340,1298 C460,1296 520,1250 620,1262 C760,1280 880,1340 1000,1320 C1100,1300 1160,1280 1200,1300 V1620 C1120,1690 1020,1730 920,1705 C820,1680 760,1660 640,1655 C480,1650 420,1570 300,1568 C160,1566 70,1610 0,1668 Z" fill="var(--slate)"/>
  <path d="M0,3210 C110,3262 250,3272 380,3252 C520,3230 610,3200 700,3232 C800,3265 850,3150 960,3148 C1060,3146 1110,3205 1200,3198 V3560 C1100,3525 1000,3560 890,3572 C740,3585 600,3566 440,3568 C280,3572 150,3600 0,3628 Z" fill="url(#violet)"/>
  <path d="M0,4400 C150,4425 300,4360 450,4378 C600,4398 660,4255 800,4232 C950,4210 1060,4300 1200,4262 V4710 H0 Z" fill="var(--navy)"/>
</svg>

<!-- Header -->
<div class="abs brand"><span class="brand-dot"></span><span>TKN<br>Music Studios</span></div>
<nav class="abs nav">
  <a href="#">HOME</a><a href="#">SERVICES</a><a href="#">MERCHANDISE</a><a href="#">FACULTY</a><a href="#">LIVE</a><a href="#">TESTIMONIAL</a><a href="#">PRE-COLLEGE</a><a href="#">REGISTRATION</a>
</nav>

<!-- Hero -->
<h1 class="abs hero-title">Take the first step<br>to learn with us</h1>
<p class="abs hero-sub">Lorem ipsum demo text area you can change the text field any time</p>
<div class="abs hero-dot"></div>
<div class="abs hero-art" role="img" aria-label="Glittering silver treble clef illustration"></div>

<!-- Perks -->
<div class="abs perk" style="left:30px;top:535px">
  <h4><svg width="22" height="16" viewBox="0 0 22 16"><path d="M1 2h8l2 2 2-2h8v12h-8l-2 1-2-1H1z" fill="none" stroke="#6b6f8e" stroke-width="1.3"/><path d="M11 4v11" stroke="#6b6f8e" stroke-width="1.3"/></svg>ADD ANYTHING</h4>
  <p>In the history of modern MUSIC, there is probably no one greater leap forward.</p>
</div>
<div class="abs perk" style="left:227px;top:535px">
  <h4><svg width="22" height="18" viewBox="0 0 22 18"><path d="M6 1h10v6a5 5 0 0 1-10 0zM11 12v3M7 17h8M6 3H2a4 4 0 0 0 4 5M16 3h4a4 4 0 0 1-4 5" fill="none" stroke="#6b6f8e" stroke-width="1.3"/></svg>ADD ANYTHING</h4>
  <p>In the history of modern MUSIC, there is probably no one greater leap forward.</p>
</div>
<div class="abs perk" style="left:423px;top:535px">
  <h4><svg width="22" height="18" viewBox="0 0 22 18"><rect x="1" y="1" width="20" height="12" fill="none" stroke="#6b6f8e" stroke-width="1.3"/><path d="M7 17h8M11 13v4" stroke="#6b6f8e" stroke-width="1.3"/></svg>ADD ANYTHING</h4>
  <p>In the history of modern MUSIC, there is probably no one greater leap forward.</p>
</div>

<!-- Popular courses -->
<h2 class="abs section-title" style="left:252px;top:706px">Popular Courses<br>Available Right Now</h2>
<p class="abs lead" style="left:252px;top:784px;width:400px">Lorem ipsum dolor sit amet, consectetur adipiscing elit, sed do eiusmod tempor incididunt ut labore et dolore magna aliqua.</p>
<div class="abs pager" style="left:868px;top:796px"><span>PREV<i></i></span><span>NEXT<i></i></span></div>

<div class="abs course" style="left:250px;top:860px"><div class="shot" role="img" aria-label="Performers on stage in red costumes"></div><p>Sample Photo Will be changed after details provided</p><p>Sample Photo Will be changed after details provided</p></div>
<div class="abs course" style="left:470px;top:860px"><div class="shot" role="img" aria-label="Performers on stage in red costumes"></div><p>Sample Photo Will be changed after details provided</p><p>Sample Photo Will be changed after details provided</p></div>
<div class="abs course" style="left:690px;top:860px"><div class="shot" role="img" aria-label="Performers on stage in red costumes"></div><p>Sample Photo Will be changed after details provided</p><p>Sample Photo Will be changed after details provided</p></div>
<div class="abs course" style="left:910px;top:860px"><div class="shot" role="img" aria-label="Performers on stage in red costumes"></div><p>Sample Photo Will be changed after details provided</p><p>Sample Photo Will be changed after details provided</p></div>
<div class="abs course" style="left:1132px;top:860px"><div class="shot" role="img" aria-label="Performers on stage in red costumes"></div></div>

<!-- Trainers live -->
<h2 class="abs white-title" style="left:240px;top:1360px">Watch Our Trainers<br>in Live Action</h2>
<p class="abs white-lead" style="left:240px;top:1438px;width:280px">In the history of modern astronomy, there is probably no one greater leap forward than the building and launch of the space telescope known as the Hubble.</p>
<div class="abs video" role="img" aria-label="Students studying together outdoors, video thumbnail"></div>
<div class="abs play"><svg width="14" height="14" viewBox="0 0 14 14"><path d="M4 2l8 5-8 5z" fill="none" stroke="#fff" stroke-width="1.4"/></svg></div>
<h4 class="abs" style="left:608px;top:1482px;font-size:11.5px;color:#fff;font-weight:700">Learn MUSIC Course for Legendary Persons</h4>
<p class="abs white-lead" style="left:608px;top:1510px;width:352px">In the history of modern MUSIC, there is probably no one greater leap forward than the building and launch of the space telescope known as the Hubble.</p>
<div class="abs pager" style="left:610px;top:1617px;color:#5a5f7d"><span>PREV<i></i></span><span>NEXT<i></i></span></div>

<!-- Services -->
<h2 class="abs section-title" style="left:240px;top:1813px">Features That<br>Can Avail By Everyone</h2>
<p class="abs" style="left:243px;top:1897px;width:200px;font-size:10px;color:#555;line-height:1.15">This is a Sample Service Section can be changed later if given enough details</p>

<div class="abs service" style="left:240px;top:1997px"><svg width="20" height="20" viewBox="0 0 20 20"><circle cx="14" cy="5" r="3" fill="none" stroke="#333" stroke-width="1.3"/><path d="M12 7L3 16M5 14l2 2" stroke="#333" stroke-width="1.3"/></svg><h4>MUSIC LESSONS</h4>Lorem ipsum dolor sit amet consec tetur adipiscing elit, sed do eiusmod tempor incididunt labore. Lorem ipsum dolor sit amet consec tetur adipiscing elit, sed do eiusmod tempor incididunt labore.</div>
<div class="abs service" style="left:240px;top:2228px"><svg width="22" height="20" viewBox="0 0 22 20"><rect x="2" y="5" width="18" height="13" fill="none" stroke="#333" stroke-width="1.3"/><path d="M8 5V2h6v3M2 10h18" stroke="#333" stroke-width="1.3" fill="none"/></svg><h4>COLLEGE PREPARATION</h4>Lorem ipsum dolor sit amet consec tetur adipiscing elit, sed do eiusmod tempor incididunt labore. Lorem ipsum dolor sit amet consec tetur adipiscing elit, sed do eiusmod tempor incididunt labore.</div>

<div class="abs service" style="left:487px;top:1895px"><svg width="22" height="22" viewBox="0 0 22 22"><path d="M7 3h8l4 4v12H7z M3 6v13h4" fill="none" stroke="#333" stroke-width="1.3"/></svg><h4>ARTIST MANAGEMENT</h4>Lorem ipsum dolor sit amet consec tetur adipiscing elit, sed do eiusmod tempor incididunt labore. Lorem ipsum dolor sit amet consec tetur adipiscing elit, sed do eiusmod tempor incididunt labore.</div>
<div class="abs service" style="left:487px;top:2126px"><svg width="22" height="20" viewBox="0 0 22 20"><path d="M2 5l5 5 4-7 4 7 5-5-2 11H4z" fill="none" stroke="#333" stroke-width="1.3"/></svg><h4>AUDITION PREPARATION</h4>Lorem ipsum dolor sit amet consec tetur adipiscing elit, sed do eiusmod tempor incididunt labore. Lorem ipsum dolor sit amet consec tetur adipiscing elit, sed do eiusmod tempor incididunt labore.</div>
<div class="abs service" style="left:487px;top:2357px"><svg width="22" height="22" viewBox="0 0 22 22"><path d="M7 3h8l4 4v12H7z M3 6v13h4" fill="none" stroke="#333" stroke-width="1.3"/></svg><h4>STUDIO DEMO RECORDING</h4>Lorem ipsum dolor sit amet consec tetur adipiscing elit, sed do eiusmod tempor incididunt labore. Lorem ipsum dolor sit amet consec tetur adipiscing elit, sed do eiusmod tempor incididunt labore.</div>

<div class="abs service" style="left:733px;top:1830px"><svg width="18" height="22" viewBox="0 0 18 22"><circle cx="9" cy="7" r="5" fill="none" stroke="#333" stroke-width="1.3"/><circle cx="9" cy="7" r="2" fill="#333"/><path d="M6 12v8l3-2 3 2v-8" fill="none" stroke="#333" stroke-width="1.3"/></svg><h4>CAREER CONSULTATION</h4>Lorem ipsum dolor sit amet consec tetur adipiscing elit, sed do eiusmod tempor incididunt labore. Lorem ipsum dolor sit amet consec tetur adipiscing elit, sed do eiusmod tempor incididunt labore.</div>
<div class="abs service" style="left:733px;top:2061px"><svg width="22" height="20" viewBox="0 0 22 20"><path d="M3 13V10a8 8 0 0 1 16 0v3" fill="none" stroke="#333" stroke-width="1.3"/><rect x="2" y="11" width="4" height="6" fill="#333"/><rect x="16" y="11" width="4" height="6" fill="#333"/></svg><h4>SONG WRITING</h4>Lorem ipsum dolor sit amet consec tetur adipiscing elit, sed do eiusmod tempor incididunt labore. Lorem ipsum dolor sit amet consec tetur adipiscing elit, sed do eiusmod tempor incididunt labore.</div>
<div class="abs service raised" style="left:733px;top:2292px;height:225px"><svg width="18" height="22" viewBox="0 0 18 22"><circle cx="9" cy="7" r="5" fill="none" stroke="#333" stroke-width="1.3"/><circle cx="9" cy="7" r="2" fill="#333"/><path d="M6 12v8l3-2 3 2v-8" fill="none" stroke="#333" stroke-width="1.3"/></svg><h4>PERFORMANCE<br>PREPARATION</h4>Lorem ipsum dolor sit amet consec tetur adipiscing elit, sed do eiusmod tempor incididunt labore. Lorem ipsum dolor sit amet consec tetur adipiscing elit, sed do eiusmod tempor incididunt labore.</div>

<!-- Testimonial -->
<div class="abs quote-mark">99</div>
<p class="abs quote">As conscious traveling Paup ers we must always be concerned about our dear Mother Earth. If you think about it, you travel across her face and She is the host to your journey.</p>
<div class="abs person">Nora Whitfield</div>
<div class="abs role">JOB TITLE, COMPANY</div>
<div class="abs portrait" role="img" aria-label="Smiling student relaxing at a laptop"></div>
<div class="abs pager" style="left:572px;top:3030px;color:#333"><span>PREV<i></i></span><span style="color:#fff">NEXT<i></i></span></div>

<!-- Trial sign-up -->
<h2 class="abs white-title" style="left:240px;top:3408px">Watch Our Trainers<br>in Live Action</h2>
<p class="abs white-lead" style="left:240px;top:3486px;width:280px">If you are looking at blank cassettes on the web, you may be very confused at the difference in price. You may see some for as low as $.17 each.</p>
<div class="abs signup">
  <h3>Courses for Free</h3>
  <small>It is high time for learning</small>
  <div class="field">NAME</div>
  <div class="field">PHONE NUMBER</div>
  <div class="field">EMAIL ADDRESS</div>
  <div class="btn">SUBMIT</div>
</div>

<!-- Gallery -->
<h2 class="abs section-title" style="left:252px;top:3718px">Features That<br>Can Avail By Everyone</h2>
<p class="abs lead" style="left:252px;top:3800px;width:180px">There is a moment in the life of any aspiring MUSICIANS that it is time to STRART. It's exciting to think about setting up your own viewing station.</p>
<div class="abs stage" style="left:246px;top:3920px;width:310px;height:195px" role="img" aria-label="Audience facing an illuminated theatre stage"></div>
<div class="abs stage" style="left:566px;top:3770px;width:309px;height:195px" role="img" aria-label="Audience facing an illuminated theatre stage"></div>
<div class="abs stage" style="left:888px;top:3705px;width:312px;height:240px" role="img" aria-label="Audience facing an illuminated theatre stage"></div>
<div class="abs tag" style="left:437px;top:3854px">Text Field</div>
<div class="abs tag" style="left:755px;top:3752px">Text Field</div>
<div class="abs tag" style="left:1075px;top:3686px">Text Field</div>

<!-- Footer -->
<div class="abs foot-col" style="left:240px;top:4415px"><h4>Top Products</h4><a href="#">Managed Website</a><a href="#">Manage Reputation</a><a href="#">Power Tools</a><a href="#">Marketing Service</a></div>
<div class="abs foot-col" style="left:363px;top:4415px"><h4>Quick Links</h4><a href="#">Title</a><a href="#">Brand Assets</a><a href="#">Social Relations</a><a href="#">Terms of Service</a></div>
<div class="abs foot-col" style="left:486px;top:4415px"><h4>Features</h4><a href="#">Feature Title</a><a href="#">Brand Assets</a><a href="#">Social Relations</a><a href="#">Terms of Service</a></div>
<div class="abs foot-col" style="left:609px;top:4415px"><h4>Resources</h4><a href="#">Guides</a><a href="#">Research</a><a href="#">Experts</a><a href="#">Agencies</a></div>
<div class="abs foot-col" style="left:733px;top:4415px"><h4>Newsletter</h4><a href="#" style="color:#a4a6c2">You can trust us. we only send promo offers.</a></div>
<div class="abs news-input">Your Email Address</div>
<div class="abs news-btn">SUBSCRIBE</div>
<p class="abs copy">Copyright ©2020 All rights reserved</p>
<div class="abs social" style="left:788px"></div>
<div class="abs social" style="left:819px"></div>
<div class="abs social" style="left:850px"></div>
<div class="abs social" style="left:881px"></div>

</div>
</body>
</html>
```